Willow Crossing: A Self Care Session for Employees

I need a flyer for organizations and businnesses. I am offering a session that will address behavioral issues such as coming to work late, not getting along with others and not working together as a team. I am a life coach who works with difficult employees, helping them address their issues and helping them be a better version of themselves. I also offer a leadership class for managers. I would like the flyer to be professional, clean and convey a feeling of trust. I would prefer to see disgns that use the color blue.

Target Market(s)

small businesses

Industry/Entity Type

Work

Font styles to use
Sans Serif

Colors
34a7d8
85cae6
0792cd
ffffff

Requirements
Must have
• shades of blue and perhaps white. should be clean, fresh and professional
Nice to have
• simple yet warm
Should not have
• distracting and heavy, playful

```html
<!DOCTYPE html>
<html lang="en">
<head>
<meta charset="utf-8">
<title>Willow Crossing: A Self Care Session for Employees</title>
<link rel="stylesheet" href="https://fonts.googleapis.com/css2?family=Open+Sans:wdth,wght@75..100,300..800&display=swap">
<style>
  :root {
    --blue: #0792cd;
    --blue-mid: #34a7d8;
    --blue-light: #85cae6;
    --white: #ffffff;
    --ink: #1a1a1a;
    --page: #eeeeee;
  }
  * { box-sizing: border-box; margin: 0; padding: 0; }
  html, body {
    width: 1200px; height: 900px; overflow: hidden;
    background: var(--page);
    font-family: "Open Sans", Arial, sans-serif;
  }
  .flyer {
    position: absolute; left: 290px; top: 40px;
    width: 620px; height: 820px;
    background: var(--white);
    overflow: hidden;
    box-shadow: 0 6px 24px rgba(0,0,0,0.12);
  }
  .hero-photo {
    position: absolute; left: 0; top: 0; width: 620px; height: 370px;
    background: linear-gradient(160deg, #f4f5f6 0%, #d9dde0 45%, #5b6470 70%, #c9ccce 100%);
  }
  .sad-face {
    position: absolute; right: 36px; top: 28px;
    font-size: 52px; font-weight: 300; color: var(--blue-mid);
    transform: rotate(90deg);
  }
  .hero-wave { position: absolute; left: 0; top: 290px; width: 620px; height: 110px; }
  .brand-badge {
    position: absolute; right: 36px; top: 300px;
    width: 124px; height: 124px; border-radius: 50%;
    background: var(--white); border: 4px solid var(--blue);
    display: flex; align-items: center; justify-content: center; text-align: center;
    font-size: 14px; font-weight: 700; color: var(--blue); line-height: 1.2;
  }
  .headline { position: absolute; left: 36px; top: 400px; color: var(--ink); }
  .headline-kicker { font-size: 30px; font-weight: 300; font-stretch: 75%; letter-spacing: 0.5px; line-height: 1; }
  .headline-main { font-size: 38px; font-weight: 800; font-stretch: 75%; line-height: 1.05; }
  .headline-accent { font-size: 60px; font-weight: 800; font-stretch: 75%; color: var(--blue); line-height: 0.95; }
  .chevrons { position: absolute; right: 36px; top: 478px; width: 90px; height: 34px; }
  .band {
    position: absolute; left: 0; width: 620px; height: 34px;
    display: flex; align-items: center; justify-content: center;
    color: var(--white); font-weight: 700; font-stretch: 80%; font-size: 18px; letter-spacing: 0.3px;
  }
  .band-question { top: 552px; background: var(--blue-mid); }
  .band-followup { top: 590px; left: 70px; width: 550px; background: var(--blue); font-size: 17px; }
  .problem { position: absolute; left: 36px; top: 664px; color: var(--ink); }
  .problem-small { font-size: 12px; font-weight: 700; text-transform: uppercase; line-height: 1.3; }
  .problem-big { font-size: 46px; font-weight: 800; font-stretch: 75%; line-height: 0.95; }
  .help-bubble { position: absolute; left: 318px; top: 636px; width: 118px; height: 62px; z-index: 2; }
  .footer-stripes { position: absolute; left: 0; bottom: 0; width: 620px; height: 110px; z-index: 1; }
  .coach { position: absolute; left: 440px; top: 638px; width: 160px; z-index: 2; }
  .coach-photo {
    width: 160px; height: 126px; border: 6px solid var(--blue-light);
    background: linear-gradient(180deg, #8c97a6 0%, #4a3a33 55%, #243a6b 100%);
  }
  .coach-name {
    margin-top: 4px; background: var(--blue); color: var(--white);
    text-align: center; font-weight: 800; font-size: 14px; padding: 4px 0; letter-spacing: 0.5px;
  }
  .contact { position: absolute; left: 36px; top: 746px; color: var(--ink); z-index: 2; }
  .contact-label { font-size: 13px; line-height: 1.15; }
  .contact-label span { border-bottom: 2px solid var(--blue-mid); }
  .contact-lines { display: flex; align-items: center; gap: 10px; margin-top: 3px; font-weight: 800; font-size: 19px; font-stretch: 85%; }
  .contact-lines .divider { width: 1px; height: 22px; background: var(--ink); }
  .contact-lines .phone { display: flex; align-items: center; gap: 4px; }
</style>
</head>
<body>
  <main class="flyer">
    <div class="hero-photo" role="img" aria-label="Photo of a tired office worker at a cluttered desk holding a paper plane"></div>
    <div class="sad-face">:(</div>
    <svg class="hero-wave" viewBox="0 0 620 110" preserveAspectRatio="none" aria-hidden="true">
      <path d="M0 40 Q80 10 150 30 T320 30 T470 20 T620 10 L620 110 L0 110 Z" fill="var(--blue)"/>
      <path d="M0 54 Q80 24 150 44 T320 44 T470 34 T620 24 L620 110 L0 110 Z" fill="var(--white)"/>
    </svg>
    <div class="brand-badge">Brightpath<br>Coaching</div>

    <header class="headline">
      <p class="headline-kicker">WILLOW CROSSING:</p>
      <h1 class="headline-main">A SELF CARE SESSION</h1>
      <p class="headline-accent">FOR EMPLOYEES</p>
    </header>
    <svg class="chevrons" viewBox="0 0 90 34" aria-hidden="true">
      <path d="M0 34 L14 0 L24 0 L10 34 Z M22 34 L36 0 L46 0 L32 34 Z M44 34 L58 0 L68 0 L54 34 Z M66 34 L80 0 L90 0 L76 34 Z" fill="var(--blue-mid)"/>
    </svg>

    <div class="band band-question">ARE YOUR EMPLOYEES BRINGING PERSONAL ISSUES ON THE JOB?</div>
    <div class="band band-followup">IS IT AFFECTING TEAM COMMUNICATION OR EVEN PRODUCTIVITY?</div>

    <section class="problem">
      <p class="problem-small">If the behavior of your manager, or</p>
      <p class="problem-big">AN EMPLOYEE</p>
      <p class="problem-small">or your entire staff is a problem</p>
    </section>

    <svg class="help-bubble" viewBox="0 0 118 62" aria-label="I can help!">
      <path d="M54 2 C84 2 104 13 104 28 C104 32 103 35 100 38 L116 52 L92 46 C82 52 69 55 54 55 C24 55 4 43 4 28 C4 13 24 2 54 2 Z" fill="var(--blue)"/>
      <text x="54" y="22" text-anchor="middle" fill="var(--white)" font-family="Open Sans, sans-serif" font-weight="700" font-size="12">I CAN</text>
      <text x="54" y="45" text-anchor="middle" fill="var(--white)" font-family="Open Sans, sans-serif" font-weight="800" font-size="22">HELP!</text>
    </svg>

    <svg class="footer-stripes" viewBox="0 0 620 110" preserveAspectRatio="none" aria-hidden="true">
      <path d="M380 110 L620 20 L620 50 L460 110 Z" fill="var(--blue-light)"/>
      <path d="M460 110 L620 50 L620 110 Z" fill="var(--blue)"/>
      <path d="M0 100 L620 86 L620 110 L0 110 Z" fill="var(--blue)"/>
    </svg>

    <figure class="coach">
      <div class="coach-photo" role="img" aria-label="Portrait photo of the life coach"></div>
      <figcaption class="coach-name">MARISA HOLT</figcaption>
    </figure>

    <section class="contact">
      <p class="contact-label">For more information<br><span>Contact on</span></p>
      <div class="contact-lines">
        <span class="phone">
          <svg width="15" height="15" viewBox="0 0 24 24" aria-hidden="true"><path d="M6.6 10.8a15 15 0 0 0 6.6 6.6l2.2-2.2c.3-.3.7-.4 1-.2 1.1.4 2.3.6 3.6.6.6 0 1 .4 1 1V20c0 .6-.4 1-1 1A17 17 0 0 1 3 4c0-.6.4-1 1-1h3.5c.6 0 1 .4 1 1 0 1.3.2 2.5.6 3.6.1.3 0 .7-.2 1z" fill="var(--ink)"/></svg>
          242-555-0148
        </span>
        <span class="divider"></span>
        <span class="phone">
          <svg width="15" height="15" viewBox="0 0 24 24" aria-hidden="true"><path d="M6.6 10.8a15 15 0 0 0 6.6 6.6l2.2-2.2c.3-.3.7-.4 1-.2 1.1.4 2.3.6 3.6.6.6 0 1 .4 1 1V20c0 .6-.4 1-1 1A17 17 0 0 1 3 4c0-.6.4-1 1-1h3.5c.6 0 1 .4 1 1 0 1.3.2 2.5.6 3.6.1.3 0 .7-.2 1z" fill="var(--ink)"/></svg>
          242-555-0193
        </span>
      </div>
    </section>
  </main>
</body>
</html>
```